Flyer für den Bereich Solarenergie
Zielgruppe
Guten Tag,
wir sind im Bereich Solarenergie tätig. Wir suchen nun Hallen mit großen Dächern, die wir anmieten können, um darauf Solaranlagen zu bauen. Wir machen dabei alles aus einer Hand. der Eigentümer muss nichts machen. Er bekommt sogar Geld von uns und das Dach ist sowieso meistens leer.
Aufgabenstellung
Wir möchten einen DINA4 Flyer den wir als PDF in Emails verschicken können. Farbdaten sollten Sie aus den Logodateien im Anhang entnehmen können. Richten Sie sich auch gerne an das Design des Logos und der Website. Dabei sollen kurz die wichtigsten Key Faktoren aufgelistet werden und das Unternehmen kurz dargestellt werden. Hier einmal die Texte:
Beschreibung zum Unternehmen:
Veltrano ist Experte für grüne Energietechnik mit über 20 Jahren Erfahrung. Mit über 1.000 zufriedenen Kunden im Bereich Photovoltaikanlagen können wir auf einen großen Erfahrungsschatz zurückgreifen. Wenn wir am Werk sind, wird nicht nur das Klima geschont, sondern auch Sie als Kunde profitieren. Mit uns wird nachhaltiges Handeln kinderleicht und gleichzeitig rentabel.
Erwirtschaften auch Sie mit Ihrem Dach nun bares Geld!
Ihre Vorteile:
- Umwelt schonen durch das Produzieren von grünem Strom
- Dach schützen vor Emissionen
- Dachsanierungen anstatt von Mietzahlungen möglich
- Keine Kosten, da wir alle Kosten der Anträge, der Anlage und aller Arbeiten übernehmen
- Mieteinnahmen generieren!
Einzige Voraussetzung:
Dachfläche mit mind. 1.500qm
Worauf warten Sie?
Nehmen Sie jetzt Kontakt auf für eine entsprechende Machbarkeitsprüfung. Natürlich ist auch das Kostenlos.
veltrano GmbH
Fennstraße 47b
48155 Münster
T: +49 176 528 914 03
E: info@veltrano-beispiel.de

```html
<!DOCTYPE html>
<html lang="de">
<head>
<meta charset="utf-8">
<title>Veltrano Energietechnik – Flyer</title>
<link href="https://fonts.googleapis.com/css2?family=Didact+Gothic&family=Nunito:wght@800;900&display=swap" rel="stylesheet">
<style>
  :root {
    --lime: #9dba36;
    --lime-mid: #8aa53a;
    --olive: #5e5a2c;
    --olive-text: #5a5527;
    --body-grey: #4f4f4f;
    --logo-grey: #3d3d3d;
    --white: #ffffff;
    --sky: #a9c6e2;
    --panel-blue: #2d4f9e;
  }
  html, body { margin: 0; padding: 0; overflow: hidden; background: var(--white); }
  .flyer {
    position: relative; width: 848px; height: 1200px; overflow: hidden;
    background: var(--white); font-family: "Didact Gothic", sans-serif;
  }
  .photo-strip { position: absolute; left: 0; top: 0; width: 848px; height: 1200px; }
  .brand { position: absolute; left: 38px; top: 22px; }
  .brand-name {
    font-family: "Didact Gothic", sans-serif; font-size: 38px; line-height: 1;
    color: var(--logo-grey); letter-spacing: -0.5px;
  }
  .brand-tagline {
    font-size: 10px; letter-spacing: 4.2px; color: var(--logo-grey); margin-top: 6px; padding-left: 2px;
  }
  .headline {
    position: absolute; left: 40px; top: 108px; margin: 0;
    font-family: "Nunito", sans-serif; font-weight: 900; font-size: 42px; line-height: 51px;
    color: var(--white);
  }
  .benefits { position: absolute; left: 0; top: 0; margin: 0; padding: 0; list-style: none; }
  .benefit { position: absolute; left: 34px; width: 400px; height: 80px; }
  .benefit-icon { position: absolute; left: 0; top: 0; width: 68px; height: 68px; }
  .benefit-text { position: absolute; left: 86px; top: -4px; width: 320px; }
  .benefit-title {
    font-family: "Nunito", sans-serif; font-weight: 800; font-size: 18px;
    color: var(--olive-text); margin: 0 0 4px;
  }
  .benefit-copy { margin: 0; font-size: 19px; line-height: 24px; color: var(--body-grey); }
  .contact-band {
    position: absolute; left: 0; top: 1039px; width: 848px; height: 78px;
    background: var(--lime); border-left: 18px solid var(--lime-mid); box-sizing: border-box;
  }
  .cta {
    position: absolute; left: 22px; top: 13px; margin: 0;
    font-family: "Nunito", sans-serif; font-weight: 800; font-size: 18px; line-height: 24px; color: var(--white);
  }
  .divider { position: absolute; left: 413px; top: 14px; width: 1px; height: 52px; background: var(--white); }
  .contact-list { position: absolute; left: 472px; top: 13px; margin: 0; padding: 0; list-style: none; }
  .contact-item {
    display: flex; align-items: center; gap: 12px; height: 24px;
    font-family: "Nunito", sans-serif; font-weight: 800; font-size: 18px; color: var(--white);
  }
  .contact-item svg { width: 18px; height: 18px; }
  .website {
    position: absolute; left: 40px; top: 1136px; margin: 0;
    font-family: "Nunito", sans-serif; font-weight: 900; font-size: 26px; color: var(--olive);
  }
</style>
</head>
<body>
<main class="flyer">

  <svg class="photo-strip" viewBox="0 0 848 1200" aria-hidden="false">
    <defs>
      <linearGradient id="roof-sky" x1="0" y1="0" x2="0" y2="1">
        <stop offset="0" stop-color="#b9d2ea"/>
        <stop offset="0.38" stop-color="#c9ccd0"/>
        <stop offset="0.5" stop-color="#6b85c0"/>
        <stop offset="1" stop-color="#2f4f9d"/>
      </linearGradient>
      <linearGradient id="bright-panels" x1="0" y1="0" x2="1" y2="1">
        <stop offset="0" stop-color="#d4dbe4"/>
        <stop offset="0.6" stop-color="#eef1f5"/>
        <stop offset="1" stop-color="#c4ccd6"/>
      </linearGradient>
      <linearGradient id="house-roof" x1="0" y1="0" x2="0" y2="1">
        <stop offset="0" stop-color="#8fb6e0"/>
        <stop offset="0.45" stop-color="#3f62b0"/>
        <stop offset="1" stop-color="#1f3b85"/>
      </linearGradient>
      <linearGradient id="roof-closeup" x1="0" y1="0" x2="1" y2="0">
        <stop offset="0" stop-color="#8a6b5a"/>
        <stop offset="0.3" stop-color="#2e4c9a"/>
        <stop offset="1" stop-color="#24408a"/>
      </linearGradient>
    </defs>

    <polygon points="325,51 523,31 509,96 315,101" fill="var(--olive)"/>
    <polygon points="325,51 509,96 315,101" fill="var(--lime-mid)"/>
    <polygon points="0,103 510,103 492,222 0,222" fill="var(--lime)"/>

    <polygon points="526,0 848,0 848,373 467,373" fill="url(#roof-sky)" role="img" aria-label="Foto: Industriehalle mit großflächiger Solaranlage auf dem Flachdach"/>
    <polygon points="463,384 848,384 848,784 401,784" fill="url(#bright-panels)" role="img" aria-label="Foto: Zwei Monteure mit Schutzhelm zwischen Solarmodulen"/>
    <polygon points="393,795 841,795 804,1039 360,1039" fill="url(#house-roof)" role="img" aria-label="Foto: Monteur installiert Solarmodule auf einem Schrägdach"/>
    <polygon points="342,1118 793,1118 780,1200 335,1200" fill="url(#roof-closeup)" role="img" aria-label="Foto: Nahaufnahme von Solarmodulen auf Dachziegeln"/>
  </svg>

  <div class="brand">
    <div class="brand-name">veltrano</div>
    <div class="brand-tagline">ENERGIETECHNIK</div>
  </div>

  <h1 class="headline">Verdienen Sie bares<br>Geld mit Ihrem Dach!</h1>

  <ul class="benefits">
    <li class="benefit" style="top:278px">
      <svg class="benefit-icon" viewBox="0 0 68 68"><circle cx="34" cy="34" r="34" fill="var(--lime-mid)"/>
        <g fill="none" stroke="#fff" stroke-width="1.6" stroke-linecap="round"><path d="M14 42c6-1 10 2 16 2h10c2 0 2-3 0-3h-8"/><path d="M22 46l8 4 16-6 8-6"/><path d="M36 36c0-8 6-13 14-13-1 8-6 13-14 13z"/><path d="M36 36c-1-6-5-9-10-9 0 5 4 9 10 9z"/></g></svg>
      <div class="benefit-text"><h2 class="benefit-title">Umweltschutz</h2><p class="benefit-copy">Umwelt schonen durch das Produzieren von grünem Strom.</p></div>
    </li>
    <li class="benefit" style="top:414px">
      <svg class="benefit-icon" viewBox="0 0 68 68"><circle cx="34" cy="34" r="34" fill="var(--lime-mid)"/>
        <g fill="none" stroke="#fff" stroke-width="1.6" stroke-linecap="round"><circle cx="34" cy="28" r="12"/><path d="M22 28h24M34 16c-5 6-5 18 0 24M34 16c5 6 5 18 0 24"/><path d="M14 30l2 14 8 8v4M54 30l-2 14-8 8v4"/></g></svg>
      <div class="benefit-text"><h2 class="benefit-title">Nachhaltig</h2><p class="benefit-copy">Ihr Dach ist vor Emissionen geschützt.</p></div>
    </li>
    <li class="benefit" style="top:542px">
      <svg class="benefit-icon" viewBox="0 0 68 68"><circle cx="34" cy="34" r="34" fill="var(--lime-mid)"/>
        <g fill="none" stroke="#fff" stroke-width="1.6" stroke-linecap="round"><rect x="20" y="14" width="28" height="40" rx="2"/><circle cx="26" cy="24" r="2"/><circle cx="26" cy="32" r="2"/><circle cx="26" cy="40" r="2"/><circle cx="26" cy="47" r="2"/><path d="M31 24h12M31 32h12M31 40h12M31 47h12"/></g></svg>
      <div class="benefit-text"><h2 class="benefit-title">Planbar</h2><p class="benefit-copy">Dachsanierungen anstatt von Mietzahlungen möglich.</p></div>
    </li>
    <li class="benefit" style="top:668px">
      <svg class="benefit-icon" viewBox="0 0 68 68"><circle cx="34" cy="34" r="34" fill="var(--lime-mid)"/>
        <g fill="none" stroke="#fff" stroke-width="1.6" stroke-linejoin="round"><rect x="17" y="26" width="24" height="26"/><rect x="15" y="21" width="28" height="6"/><path d="M29 21v31"/><path d="M29 21c-4-6-10-6-9-1M29 21c4-6 10-6 9-1"/><path d="M40 36l8-8 7 7-8 8z"/></g></svg>
      <div class="benefit-text"><h2 class="benefit-title">Kostenfrei</h2><p class="benefit-copy">Wir übernehmen alle Kosten der Anträge, der Anlage und aller Arbeiten.</p></div>
    </li>
    <li class="benefit" style="top:796px">
      <svg class="benefit-icon" viewBox="0 0 68 68"><circle cx="34" cy="34" r="34" fill="var(--lime-mid)"/>
        <path d="M28 14l6 4 6-4-3 8h-6z M24 26h20c8 8 10 26-10 26s-18-18-10-26z" fill="#fff"/>
        <text x="34" y="46" text-anchor="middle" font-family="Didact Gothic, sans-serif" font-size="16" fill="var(--lime-mid)">€</text></svg>
      <div class="benefit-text"><h2 class="benefit-title">Zuverdienst</h2><p class="benefit-copy">Sie generieren durch uns Mieteinnahmen.</p></div>
    </li>
    <li class="benefit" style="top:923px">
      <svg class="benefit-icon" viewBox="0 0 68 68"><circle cx="34" cy="34" r="34" fill="var(--olive-text)"/>
        <g fill="none" stroke="#fff" stroke-width="1.6"><path d="M6 40l24-16 32 18"/><path d="M11 37l19-11 26 15"/><path d="M19 31v-5h3v3"/></g></svg>
      <div class="benefit-text"><h2 class="benefit-title">Voraussetzung</h2><p class="benefit-copy">Dachfläche mit mind. 1.500qm.</p></div>
    </li>
  </ul>

  <section class="contact-band">
    <p class="cta">Kontaktieren Sie uns jetzt für eine<br>kostenlose Machbarkeitsprüfung!</p>
    <span class="divider"></span>
    <ul class="contact-list">
      <li class="contact-item"><svg viewBox="0 0 24 24"><path fill="#fff" d="M6.6 10.8a15 15 0 0 0 6.6 6.6l2.2-2.2c.3-.3.7-.4 1-.2 1.1.4 2.3.6 3.6.6.6 0 1 .4 1 1V20c0 .6-.4 1-1 1A17 17 0 0 1 3 4c0-.6.4-1 1-1h3.5c.6 0 1 .4 1 1 0 1.3.2 2.5.6 3.6.1.3 0 .7-.2 1z"/></svg>+49 176 528 914 03</li>
      <li class="contact-item"><svg viewBox="0 0 24 24"><rect x="2" y="5" width="20" height="14" fill="#fff"/><path d="M2 5l10 8 10-8M2 19l8-7M22 19l-8-7" fill="none" stroke="var(--lime)" stroke-width="1.5"/></svg>info@veltrano-beispiel.de</li>
    </ul>
  </section>

  <p class="website">www.veltrano-beispiel.de</p>
</main>
</body>
</html>
```